Fernhollow Services

After a high quality design website. we are a company that provides services to people that own land and need a hand getting on top of the delayed jobs.
would want a number of tab/ pages for the web page.
Home page / About us page / services page / Gallery page. / Contact us page
we offer a wide range of services .listed below

Stock Work (title)

Stock movement
Break feeding
Temporary staffing

Spraying (title)

Spraying weeds
Spraying gorse

Pastures (title)

Fertilizing
Topping

Building (title)

Habitable sheds
Farm sheds
Sheep yards
Cattle yards
Repair farm buildings
Decks
Retaining walls

Fencing (title)

Stock fencing
Post & rail
Stock yards repair
Electric fencing install & repairs

Water Management (title)

Water trough installation
Water scheme install
Water trough cleaning
Farm water maintenance
Water ponds
Ornamental ponds
Drainage

General (title)

Lawn mowing
Hedge trimming
Pruning trees
Metaling drive ways & races
Water blasting
Small digger work
Little tip truck cartage
Home kill management
Mulching gorse
Section clearing

```html
<!DOCTYPE html>
<html lang="en">
<head>
<meta charset="utf-8">
<title>Fernhollow Services</title>
<link href="https://fonts.googleapis.com/css2?family=Montserrat:wght@500;600;700;800&family=Open+Sans:ital,wght@0,400;0,600;1,400&display=swap" rel="stylesheet">
<style>
:root{
  --green:#5b9b16;
  --green-dark:#4a8410;
  --green-bright:#6aab1f;
  --pale:#f2fbe7;
  --ink:#1b1b1b;
  --muted:#555;
  --footer:#1f2a19;
  --star:#f2b705;
  --white:#fff;
}
*{box-sizing:border-box;margin:0;padding:0}
html,body{width:1200px;height:5150px;overflow:hidden}
body{font-family:"Open Sans",Arial,sans-serif;color:var(--ink);background:var(--white);position:relative}
section,header,footer{position:relative;width:1200px;overflow:hidden}
.abs{position:absolute}
.btn{display:inline-flex;align-items:center;gap:6px;font-family:"Montserrat",Arial,sans-serif;font-weight:700;font-size:15px;border-radius:22px;text-transform:uppercase;white-space:nowrap}
.btn-solid{background:var(--green);color:#fff;padding:11px 30px}
.btn-line{border:2px solid var(--green);color:var(--green);padding:9px 22px;background:#fff}
.btn-line-white{border:2px solid #fff;color:#fff;padding:9px 38px}
.arrow-dot{width:13px;height:13px;border-radius:50%;background:#fff;display:inline-block;position:relative}
.arrow-dot::after{content:"";position:absolute;left:4px;top:3.5px;border-left:6px solid var(--green);border-top:3px solid transparent;border-bottom:3px solid transparent}
.btn-line .arrow-dot{background:var(--green)}
.btn-line .arrow-dot::after{border-left-color:#fff}
.section-title{font-family:"Montserrat",Arial,sans-serif;font-weight:800;font-size:38px;text-align:center;letter-spacing:.5px}
.section-title span{color:var(--green)}
.title-bar{width:90px;height:4px;background:var(--green);margin:8px auto 0}

/* header */
.site-header{height:104px;border-top:3px solid var(--green)}
.brand{left:100px;top:20px;display:flex;align-items:center;gap:10px}
.brand-dot{width:48px;height:48px;border-radius:50%;border:3px solid var(--green)}
.brand-name{font-family:"Montserrat",Arial,sans-serif;font-weight:700;font-size:24px;color:var(--green);white-space:nowrap}
.top-contact{top:10px;display:flex;align-items:center;gap:8px;font-size:14px;font-weight:600;white-space:nowrap}
.top-contact small{display:block;font-size:10px;font-weight:400;color:#444}
.ic-circle{width:32px;height:32px;border-radius:50%;border:1.5px solid var(--green);display:flex;align-items:center;justify-content:center}
.nav{top:64px;left:478px;display:flex;gap:56px;font-family:"Montserrat",Arial,sans-serif;font-weight:500;font-size:16px;text-transform:uppercase;white-space:nowrap}

/* hero */
.hero{height:680px}
.hero-photo{position:absolute;inset:0;background:linear-gradient(180deg,#c9b8b4 0%,#e7cdbd 30%,#9eae7b 45%,#5d8a2a 62%,#3f6f1a 100%)}
.hero h1{position:absolute;left:100px;top:182px;font-family:"Montserrat",Arial,sans-serif;font-weight:800;font-size:50px;line-height:46px;color:#111}
.hero p{position:absolute;left:100px;top:296px;width:400px;font-size:15px;line-height:28px;color:#111}
.hero .btn{position:absolute;left:100px;top:376px}
.dots{position:absolute;left:104px;top:460px;display:flex;gap:12px}
.dots i{width:12px;height:12px;border-radius:50%;border:2px solid #fff}
.dots i.on{background:#fff}
.hero-wave{position:absolute;left:0;bottom:0}

/* about */
.about{height:550px;background:var(--pale)}
.about-photo{position:absolute;left:143px;top:40px;width:452px;height:452px;border-radius:50%;border:4px solid var(--green);background:radial-gradient(circle at 50% 30%,#d9c79e,#6f8f3a 55%,#345a1a)}
.about-text{position:absolute;left:665px;top:90px;width:440px}
.about-text h2{font-family:"Montserrat",Arial,sans-serif;font-weight:800;font-size:38px}
.about-text h2 span{color:var(--green)}
.about-text p{font-size:15px;line-height:28px;color:#333;margin-top:16px}
.about-text .btn{margin-top:20px}

/* services */
.services{height:1045px}
.services .section-title{padding-top:70px}
.svc-grid{position:absolute;left:100px;top:164px;display:grid;grid-template-columns:repeat(3,312px);column-gap:32px;row-gap:44px}
.svc{position:relative;height:326px}
.svc-img{height:226px;border-radius:3px}
.svc-card{position:absolute;left:16px;right:16px;top:162px;height:166px;background:#fff;box-shadow:0 2px 10px rgba(0,0,0,.12);text-align:center;padding-top:26px}
.svc-card h3{font-family:"Montserrat",Arial,sans-serif;font-weight:700;font-size:19px;text-transform:uppercase}
.svc-card p{font-size:13px;line-height:25px;color:#444;margin:8px 12px 0}
.go{position:absolute;left:50%;bottom:-12px;margin-left:-16px;width:32px;height:32px;border-radius:50%;background:var(--green);display:flex;align-items:center;justify-content:center}
.svc-general{position:absolute;left:100px;right:100px;top:880px;text-align:center;font-size:13px;color:#444}
.svc-general b{font-family:"Montserrat",Arial,sans-serif;font-weight:700;color:var(--green);text-transform:uppercase;margin-right:8px}
.svc-all{position:absolute;left:488px;top:930px}

/* why choose */
.why{height:665px;background:var(--pale)}
.why .section-title{padding-top:66px}
.why-photo{position:absolute;left:418px;top:250px;width:366px;height:366px;border-radius:50%;background:radial-gradient(circle at 50% 35%,#bba58c,#6b7a45 50%,#8c2f3c 85%)}
.why-item{position:absolute;width:360px}
.why-item h4{font-family:"Montserrat",Arial,sans-serif;font-weight:700;font-size:17px;text-transform:uppercase}
.why-item p{font-size:13.5px;line-height:26px;color:#444;margin-top:6px}
.why-item.r{text-align:right}
.why-ic{position:absolute;width:96px;height:96px;border-radius:50%;background:#fff;border:1px solid #e3ead8;display:flex;align-items:center;justify-content:center}

/* gallery */
.gallery{height:685px;background:linear-gradient(180deg,#5d9d1c,#4f8d14)}
.gallery .section-title{color:#fff;padding-top:62px}
.gallery .section-title span{color:#fff}
.gallery .title-bar{background:#fff}
.gal{position:absolute;border-radius:2px}
.gal-more{position:absolute;left:504px;top:572px}

/* testimonial */
.testi{height:500px}
.testi .section-title{color:var(--green);padding-top:62px}
.t-card{position:absolute;top:155px;width:312px;height:252px;background:#fff;border:1px solid #e7e7e7;box-shadow:0 0 0 6px #f6f6f6 inset;text-align:center;padding-top:22px}
.quote{font-family:"Montserrat",Arial,sans-serif;font-weight:800;font-size:50px;line-height:40px;color:var(--green)}
.stars{color:var(--star);font-size:17px;letter-spacing:1px;margin-top:6px}
.t-card p{font-style:italic;font-size:13px;line-height:25px;color:#444;margin:12px 18px 0}
.t-card h5{font-family:"Montserrat",Arial,sans-serif;font-weight:700;font-size:14px;margin-top:8px}

/* contact */
.contact{height:595px;background:linear-gradient(90deg,#4f8d14,#63a41d 60%,#5b9b16)}
.contact-photo{position:absolute;left:0;top:0;width:1200px;height:595px;background:radial-gradient(ellipse at 42% 40%,rgba(40,80,10,.22),rgba(40,80,10,0) 60%)}
.contact h2{position:absolute;left:100px;top:108px;font-family:"Montserrat",Arial,sans-serif;font-weight:800;font-size:38px;color:#fff}
.contact .intro{position:absolute;left:100px;top:174px;width:480px;font-size:14px;line-height:26px;color:#fff}
.c-row{position:absolute;left:118px;display:flex;align-items:center;gap:18px;color:#fff;white-space:nowrap}
.c-ic{width:64px;height:64px;border-radius:50%;background:#fff;border:5px solid rgba(255,255,255,.45);background-clip:padding-box;display:flex;align-items:center;justify-content:center}
.c-row small{display:block;font-size:14px;font-weight:600}
.c-row b{font-size:19px;font-weight:600}
.form{position:absolute;left:662px;top:68px;width:438px;height:458px;background:#fff;border-radius:3px;padding:22px 28px 0 40px}
.form label{display:block;font-size:12px;line-height:16px;font-weight:600;margin-bottom:4px}
.field{height:40px;border:1px solid #ddd;font-size:11px;color:#888;padding:10px 12px;margin-bottom:18px}
.field.big{height:120px;margin-bottom:22px}
.form .btn{margin-left:88px;padding:11px 38px}

/* footer */
.site-footer{height:330px;background:var(--footer);color:#fff}
.f-brand{position:absolute;left:100px;top:74px;display:flex;align-items:center;gap:12px}
.f-brand .brand-dot{border-color:#fff}
.f-brand .brand-name{color:#fff;font-size:28px}
.socials{position:absolute;left:155px;top:196px;display:flex;gap:15px}
.socials i{width:38px;height:38px;border-radius:50%;background:var(--green-bright)}
.f-col{position:absolute;top:62px}
.f-col h6{font-family:"Montserrat",Arial,sans-serif;font-weight:600;font-size:18px;margin-bottom:14px}
.f-col li{list-style:none;font-size:13px;line-height:30px}
.f-col p{font-size:13px;line-height:22px}
.f-rule{position:absolute;left:100px;right:100px;top:268px;border-top:1px solid rgba(255,255,255,.12)}
.copy{position:absolute;left:0;right:0;top:290px;text-align:center;font-size:14px}
</style>
</head>
<body>

<header class="site-header">
  <div class="abs brand"><span class="brand-dot"></span><span class="brand-name">Fernhollow Services</span></div>
  <div class="abs top-contact" style="left:644px">
    <span class="ic-circle"><svg width="14" height="14" viewBox="0 0 24 24"><path d="M6.6 10.8a15 15 0 0 0 6.6 6.6l2.2-2.2c.3-.3.7-.4 1-.2 1.1.4 2.3.6 3.6.6.6 0 1 .4 1 1V20c0 .6-.4 1-1 1A17 17 0 0 1 3 4c0-.6.4-1 1-1h3.5c.6 0 1 .4 1 1 0 1.3.2 2.5.6 3.6.1.3 0 .7-.2 1z" fill="#5b9b16"/></svg></span>
    <div><small>CALL US</small>+1 555-014-2290</div>
  </div>
  <div class="abs top-contact" style="left:824px">
    <span class="ic-circle"><svg width="14" height="14" viewBox="0 0 24 24"><rect x="2" y="5" width="20" height="14" rx="1" fill="none" stroke="#5b9b16" stroke-width="2"/><path d="M2 6l10 7 10-7" fill="none" stroke="#5b9b16" stroke-width="2"/></svg></span>
    <div><small>EMAIL US</small>info@fernhollowservices.com</div>
  </div>
  <nav class="abs nav"><span>Home</span><span>About Us</span><span>Services</span><span>Gallery</span><span>Contact Us</span></nav>
</header>

<section class="hero">
  <div class="hero-photo" role="img" aria-label="Tractor spraying rows of crops in a green field at sunrise"></div>
  <h1>FERNHOLLOW<br>SERVICES</h1>
  <p>Lorem ipsum dolor sit amet,ctetur adipiscing elit, sed do eiusmod tempor incididunt ut labore</p>
  <span class="btn btn-solid">Get Started <i class="arrow-dot"></i></span>
  <div class="dots"><i></i><i class="on"></i><i></i><i></i></div>
  <svg class="hero-wave" width="1200" height="130" viewBox="0 0 1200 130"><path d="M0 130 C180 60 360 40 560 80 S900 110 1200 0 L1200 130 Z" fill="#f2fbe7"/><path d="M0 122 C180 52 360 32 560 72 S900 102 1200 -8" fill="none" stroke="#5b9b16" stroke-width="4"/></svg>
</section>

<section class="about">
  <div class="about-photo" role="img" aria-label="Two farmers inspecting young corn plants in a field"></div>
  <div class="about-text">
    <h2>ABOUT <span>US</span></h2>
    <p>Lorem ipsum dolor sit amet, consectetur adipiscdo eiusmod tempor incididunt ut laboreis ipsum suspendiytrices gravida. Risus commodo viverra maecean lacus vel facilisis. Lorem ipsum dolor sit amet</p>
    <p>Lorem ipsum dolor sit amet, consectetur adipiscdo eiusmod tempor incididunt ut laboreis ipsum suspendiytrices gravida. Risus commodo viverra</p>
    <span class="btn btn-solid">Learn More <i class="arrow-dot"></i></span>
  </div>
</section>

<section class="services">
  <h2 class="section-title">OUR <span>SERVICES</span></h2>
  <div class="title-bar"></div>
  <div class="svc-grid">
    <div class="svc"><div class="svc-img" role="img" aria-label="Hands holding soil in a paddock" style="background:linear-gradient(160deg,#7d8a6a,#4e5a3a)"></div><div class="svc-card"><h3>Stock Work</h3><p>Lorem ipsum dolor sit amet, cnsectetur adipiscdo eiusmod tempor incididunt ut laboreis ipsum suspendiy</p><span class="go"><svg width="10" height="12"><path d="M2 1l6 5-6 5" fill="none" stroke="#fff" stroke-width="2"/></svg></span></div></div>
    <div class="svc"><div class="svc-img" role="img" aria-label="Worker spraying crops with a backpack sprayer" style="background:linear-gradient(160deg,#b8c3b0,#4f7a30)"></div><div class="svc-card"><h3>Spraying</h3><p>Lorem ipsum dolor sit amet, cnsectetur adipiscdo eiusmod tempor incididunt ut laboreis ipsum suspendiy</p><span class="go"><svg width="10" height="12"><path d="M2 1l6 5-6 5" fill="none" stroke="#fff" stroke-width="2"/></svg></span></div></div>
    <div class="svc"><div class="svc-img" role="img" aria-label="Scoop of fertiliser granules over dark soil" style="background:linear-gradient(160deg,#4a3a2c,#2b3b2a)"></div><div class="svc-card"><h3>Pastures</h3><p>Lorem ipsum dolor sit amet, cnsectetur adipiscdo eiusmod tempor incididunt ut laboreis ipsum suspendiy</p><span class="go"><svg width="10" height="12"><path d="M2 1l6 5-6 5" fill="none" stroke="#fff" stroke-width="2"/></svg></span></div></div>
    <div class="svc"><div class="svc-img" role="img" aria-label="Farmer with a herd of cattle in a yard" style="background:linear-gradient(160deg,#cdbfa6,#7a4a30)"></div><div class="svc-card"><h3>Building</h3><p>Lorem ipsum dolor sit amet, cnsectetur adipiscdo eiusmod tempor incididunt ut laboreis ipsum suspendiy</p><span class="go"><svg width="10" height="12"><path d="M2 1l6 5-6 5" fill="none" stroke="#fff" stroke-width="2"/></svg></span></div></div>
    <div class="svc"><div class="svc-img" role="img" aria-label="Wire fence and wooden post across green pasture" style="background:linear-gradient(160deg,#8fbf4a,#3f7a1a)"></div><div class="svc-card"><h3>Fencing</h3><p>Lorem ipsum dolor sit amet, cnsectetur adipiscdo eiusmod tempor incididunt ut laboreis ipsum suspendiy</p><span class="go"><svg width="10" height="12"><path d="M2 1l6 5-6 5" fill="none" stroke="#fff" stroke-width="2"/></svg></span></div></div>
    <div class="svc"><div class="svc-img" role="img" aria-label="Hands fitting an irrigation pipe connector" style="background:linear-gradient(160deg,#5a6a7a,#2f3e2a)"></div><div class="svc-card"><h3>Water Management</h3><p>Lorem ipsum dolor sit amet, cnsectetur adipiscdo eiusmod tempor incididunt ut laboreis ipsum suspendiy</p><span class="go"><svg width="10" height="12"><path d="M2 1l6 5-6 5" fill="none" stroke="#fff" stroke-width="2"/></svg></span></div></div>
  </div>
  <p class="svc-general"><b>General</b>Lawn mowing · Hedge trimming · Pruning trees · Metaling drive ways &amp; races · Water blasting · Small digger work · Section clearing</p>
  <span class="btn btn-line svc-all">View All Services <i class="arrow-dot"></i></span>
</section>

<section class="why">
  <h2 class="section-title">WHY CHOOSE <span>US</span></h2>
  <div class="title-bar"></div>
  <svg class="abs" style="left:0;top:0" width="1200" height="665"><path d="M367 550 A260 260 0 0 1 833 550" fill="none" stroke="#8fb863" stroke-width="2" stroke-dasharray="3 6"/><circle cx="367" cy="552" r="6" fill="#5b9b16"/><circle cx="836" cy="552" r="6" fill="#5b9b16"/></svg>
  <div class="why-photo" role="img" aria-label="Farmer using a tablet among rows of red flowers"></div>
  <div class="why-item r" style="left:22px;top:206px"><h4>Finibus Bonorum</h4><p>Lorem ipsum dolor sit et, cnsectetur<br>adipiscdo eiusmod tempor</p></div>
  <div class="why-ic" style="left:392px;top:192px"><svg width="40" height="40"><circle cx="20" cy="20" r="12" fill="none" stroke="#5b9b16" stroke-width="2"/><path d="M14 20l5 5 8-9" fill="none" stroke="#5b9b16" stroke-width="2"/></svg></div>
  <div class="why-item" style="left:816px;top:206px"><h4>Finibus Bonorum</h4><p>Lorem ipsum dolor sit et, cnsectetur<br>adipiscdo eiusmod tempor</p></div>
  <div class="why-ic" style="left:712px;top:192px"><svg width="40" height="40"><circle cx="20" cy="20" r="12" fill="none" stroke="#5b9b16" stroke-width="2"/><path d="M14 20l5 5 8-9" fill="none" stroke="#5b9b16" stroke-width="2"/></svg></div>
  <div class="why-item r" style="left:-76px;top:412px"><h4>Finibus Bonorum</h4><p>Lorem ipsum dolor sit et, cnsectetur<br>adipiscdo eiusmod tempor</p></div>
  <div class="why-ic" style="left:292px;top:398px"><svg width="40" height="40"><circle cx="20" cy="20" r="12" fill="none" stroke="#5b9b16" stroke-width="2"/><path d="M14 20l5 5 8-9" fill="none" stroke="#5b9b16" stroke-width="2"/></svg></div>
  <div class="why-item" style="left:916px;top:412px"><h4>Finibus Bonorum</h4><p>Lorem ipsum dolor sit et, cnsectetur<br>adipiscdo eiusmod tempor</p></div>
  <div class="why-ic" style="left:812px;top:398px"><svg width="40" height="40"><circle cx="20" cy="20" r="12" fill="none" stroke="#5b9b16" stroke-width="2"/><path d="M14 20l5 5 8-9" fill="none" stroke="#5b9b16" stroke-width="2"/></svg></div>
</section>

<section class="gallery">
  <h2 class="section-title">OUR <span>GALLERY</span></h2>
  <div class="title-bar"></div>
  <div class="gal" role="img" aria-label="Tractor towing a chain harrow across a paddock" style="left:100px;top:148px;width:474px;height:392px;background:linear-gradient(180deg,#b9c9d6 0%,#7f9a5e 30%,#6a7f42 100%)"></div>
  <div class="gal" role="img" aria-label="Green tractor with a red mulcher attachment" style="left:588px;top:148px;width:248px;height:190px;background:linear-gradient(160deg,#c9cfd4,#b23a2a 60%,#3d6b1f)"></div>
  <div class="gal" role="img" aria-label="Compact tractor on a trailer with loading ramps" style="left:850px;top:148px;width:248px;height:190px;background:linear-gradient(160deg,#d8dde0,#4e7a2a 55%,#5a5a5a)"></div>
  <div class="gal" role="img" aria-label="Utility vehicle towing a trailer with blue equipment" style="left:588px;top:352px;width:248px;height:190px;background:linear-gradient(160deg,#a9c0d8,#2f5fa0 50%,#3e6a2a)"></div>
  <div class="gal" role="img" aria-label="Green tractor with a front loader fork attachment" style="left:850px;top:352px;width:248px;height:190px;background:linear-gradient(160deg,#b7cbd7,#3f8a1c 55%,#3b5a24)"></div>
  <span class="btn btn-line-white gal-more">View More <i class="arrow-dot"></i></span>
</section>

<section class="testi">
  <h2 class="section-title">TESTIMONIAL</h2>
  <div class="title-bar"></div>
  <div class="t-card" style="left:100px"><div class="quote">&ldquo;</div><div class="stars">★★★★★</div><p>Sed ut perspiciatis unde ois iste natus error sit voluptatemtium doloremque laudantium, totam rem aperiam, eaque ipsa quae ab illo inventore veritatis et</p><h5>- ARA MITCHELL</h5></div>
  <div class="t-card" style="left:444px"><div class="quote">&ldquo;</div><div class="stars">★★★★★</div><p>Sed ut perspiciatis unde ois iste natus error sit voluptatemtium doloremque laudantium, totam rem aperiam, eaque ipsa quae ab illo inventore veritatis et</p><h5>- ARA MITCHELL</h5></div>
  <div class="t-card" style="left:788px"><div class="quote">&ldquo;</div><div class="stars">★★★★★</div><p>Sed ut perspiciatis unde ois iste natus error sit voluptatemtium doloremque laudantium, totam rem aperiam, eaque ipsa quae ab illo inventore veritatis et</p><h5>- ARA MITCHELL</h5></div>
</section>

<section class="contact">
  <div class="contact-photo" role="img" aria-label="Faint background of a farmer tending crops"></div>
  <h2>CONTACT US</h2>
  <p class="intro">Lorem ipsum dolor sit amet, cnsectetur adipiscdo eiusmod tempor incididunt ut laboreis ipsum suspendiy</p>
  <div class="c-row" style="top:262px"><span class="c-ic"><svg width="24" height="24" viewBox="0 0 24 24"><path d="M12 2a7 7 0 0 0-7 7c0 5 7 13 7 13s7-8 7-13a7 7 0 0 0-7-7z" fill="none" stroke="#5b9b16" stroke-width="2"/><circle cx="12" cy="9" r="2.5" fill="#5b9b16"/></svg></span><div><small>Location:</small><b>48 Ridgeline Rd Hollowvale, US 40210</b></div></div>
  <div class="c-row" style="top:346px"><span class="c-ic"><svg width="22" height="22" viewBox="0 0 24 24"><path d="M6.6 10.8a15 15 0 0 0 6.6 6.6l2.2-2.2c.3-.3.7-.4 1-.2 1.1.4 2.3.6 3.6.6.6 0 1 .4 1 1V20c0 .6-.4 1-1 1A17 17 0 0 1 3 4c0-.6.4-1 1-1h3.5c.6 0 1 .4 1 1 0 1.3.2 2.5.6 3.6.1.3 0 .7-.2 1z" fill="#5b9b16"/></svg></span><div><small>Phone:</small><b>+1 555-014-2290</b></div></div>
  <div class="c-row" style="top:430px"><span class="c-ic"><svg width="24" height="24" viewBox="0 0 24 24"><rect x="2" y="5" width="20" height="14" rx="1" fill="none" stroke="#5b9b16" stroke-width="2"/><path d="M2 6l10 7 10-7" fill="none" stroke="#5b9b16" stroke-width="2"/></svg></span><div><small>Email Us:</small><b>info@fernhollowservices.com</b></div></div>
  <div class="form">
    <label>Your Name</label><div class="field">Enter Your Name</div>
    <label>Your Email</label><div class="field">Enter Your Email</div>
    <label>Your Phone</label><div class="field">Enter Your Phone Number</div>
    <label>Message</label><div class="field big">Enter Your Message</div>
    <span class="btn btn-solid">Submit Now <i class="arrow-dot"></i></span>
  </div>
</section>

<footer class="site-footer">
  <div class="f-brand"><span class="brand-dot"></span><span class="brand-name">Fernhollow Services</span></div>
  <div class="socials"><i></i><i></i><i></i><i></i></div>
  <div class="f-col" style="left:520px"><h6>Quick Links</h6><ul><li>Home</li><li>About Us</li><li>Services</li><li>Gallery</li><li>Contact Us</li></ul></div>
  <div class="f-col" style="left:700px"><h6>Other Links</h6><ul><li>Contact Sales</li><li>Legal Hub</li><li>Privacy Policy</li><li>Trust &amp; Security</li><li>Cookie Preferences</li></ul></div>
  <div class="f-col" style="left:896px"><h6>Contact Info</h6><p>48 Ridgeline Rd<br>Hollowvale, US 40210</p><p style="margin-top:8px">+1 555 - 014 - 2290</p><p style="margin-top:8px">info@fernhollowservices.com</p></div>
  <div class="f-rule"></div>
  <div class="copy">©Copyright 2024 Fernhollow Services. All Rights Reserved.</div>
</footer>

</body>
</html>
```